findnearhub.org - creative brochure
findnearhub.org
Visit our website - findnearhub.org
Internet Services
Brick and mortar local businesses
The brochure needs to demonstrate confidence, affordability, and exclusivity.
The text for the brochure can be found on the website findnearhub.org
The design can be a 3 fold or rack card style… whatever turns out best

```html
<!DOCTYPE html>
<html lang="en">
<head>
<meta charset="utf-8">
<title>findnearhub.org – Tri-fold Brochure</title>
<link href="https://fonts.googleapis.com/css2?family=Arimo:wght@400;700&display=swap" rel="stylesheet">
<style>
  :root{
    --red:#c8161d;
    --red-dark:#9e0f14;
    --ink:#2b2b2b;
    --paper:#f1f1f1;
    --panel-light:#f7f7f7;
    --panel-grey:#d9d9d9;
    --box-dark:#1f1f1f;
    --box-mid:#4a4a4a;
    --fold:#d0d0d0;
  }
  *{box-sizing:border-box;margin:0;padding:0}
  html,body{width:1200px;height:932px;overflow:hidden;background:#fff}
  body{font-family:"Arimo",Arial,sans-serif;color:var(--ink)}
  .brochure{position:relative;width:1200px;height:932px;background:var(--paper)}
  .fold{position:absolute;top:0;width:1px;height:932px;background:var(--fold)}
  .abs{position:absolute}
  p{font-size:14.5px;line-height:1.32}

  /* ribbons */
  .ribbon{position:absolute;background:linear-gradient(var(--red),var(--red-dark));color:#fff;
    font-weight:700;text-transform:uppercase;display:flex;align-items:center;letter-spacing:.3px}
  .ribbon--right{clip-path:polygon(0 0,calc(100% - 22px) 0,100% 50%,calc(100% - 22px) 100%,0 100%)}

  /* dark title box + grey panel */
  .panel-card{position:absolute;border-radius:10px;
    background:linear-gradient(180deg,var(--panel-grey),var(--panel-light));
    box-shadow:0 2px 5px rgba(0,0,0,.25)}
  .card-title{position:absolute;left:0;right:0;top:0;border-radius:8px;
    background:linear-gradient(180deg,var(--box-mid),var(--box-dark) 60%);color:#fff;
    font-weight:700;text-transform:uppercase;display:flex;align-items:center;justify-content:center;
    box-shadow:0 3px 6px rgba(0,0,0,.4)}
  .card-body{position:absolute;left:20px;right:20px}
  .card-body p{margin-bottom:16px}
  .cta{color:var(--red);font-weight:700}

  /* lists */
  .benefits{list-style:none}
  .benefits li{display:flex;align-items:center;gap:10px;color:var(--red);font-weight:700;
    font-size:14.5px;text-transform:uppercase;margin-bottom:15px}
  .features{list-style:none}
  .features li{font-size:11px;font-weight:700;line-height:16px;display:flex;gap:6px}
  .features li::before{content:"";width:5px;height:5px;background:var(--ink);margin-top:5px;flex:none}
</style>
</head>
<body>
<main class="brochure">
  <span class="fold" style="left:396px"></span>
  <span class="fold" style="left:797px"></span>

  <!-- LEFT PANEL -->
  <section class="panel panel--left">
    <div class="abs" role="img" aria-label="Map with a location pin marker"
         style="left:0;top:0;width:150px;height:140px;background:linear-gradient(135deg,#d8d8d8,#a9b8a6 55%,#6fb6d8);border-radius:0 0 10px 0"></div>
    <p class="abs" style="left:170px;top:22px;width:214px">As the Internet evolves and web users become more sophisticated, local consumers are turning more and more to the Internet to find products and services on a local basis.</p>
    <p class="abs" style="left:22px;top:155px;width:362px">We'll get your website listed in Seekly places, Lookwise and Findora local for amazing local visibility. Everytime a local consumer searches for your product or service, you'll be there in perfect view.</p>

    <div class="ribbon ribbon--right" style="left:0;top:278px;width:382px;height:32px;padding-left:14px;font-size:15px">We can help your business...</div>
    <ul class="benefits abs" style="left:22px;top:338px">
      <li><svg width="16" height="16" viewBox="0 0 16 16"><path d="M2 8l4 4 8-9" stroke="#c8161d" stroke-width="3" fill="none"/></svg>Eliminate pay per click charges</li>
      <li><svg width="16" height="16" viewBox="0 0 16 16"><path d="M2 8l4 4 8-9" stroke="#c8161d" stroke-width="3" fill="none"/></svg>Enhance your local search listings</li>
      <li><svg width="16" height="16" viewBox="0 0 16 16"><path d="M2 8l4 4 8-9" stroke="#c8161d" stroke-width="3" fill="none"/></svg>Reduce your advertising budget</li>
      <li><svg width="16" height="16" viewBox="0 0 16 16"><path d="M2 8l4 4 8-9" stroke="#c8161d" stroke-width="3" fill="none"/></svg>Increase profits</li>
      <li><svg width="16" height="16" viewBox="0 0 16 16"><path d="M2 8l4 4 8-9" stroke="#c8161d" stroke-width="3" fill="none"/></svg>Acquire new customers</li>
      <li><svg width="16" height="16" viewBox="0 0 16 16"><path d="M2 8l4 4 8-9" stroke="#c8161d" stroke-width="3" fill="none"/></svg>Gain visibility over your competition</li>
    </ul>

    <div class="ribbon ribbon--right" style="left:0;top:636px;width:228px;height:40px;padding-left:18px;font-size:19px">Our services</div>
    <p class="abs" style="left:22px;top:706px;width:362px">We specialize in getting localized results in the search engines i.e., if you are an appliance repair company in Langley, BC you will want us... your LOCAL SEO experts to optimize your local presence, allowing you to capture all the local customers searching specifically for your products or services.</p>
  </section>

  <!-- MIDDLE PANEL -->
  <section class="panel panel--middle">
    <div class="abs" role="img" aria-label="Search bar illustration with the word Search"
         style="left:480px;top:28px;width:230px;height:88px;background:linear-gradient(180deg,#e6e6e6,#cfcfcf);border-radius:8px"></div>

    <div class="panel-card" style="left:417px;top:180px;width:366px;height:400px">
      <div class="card-title" style="height:58px;font-size:24px">Search + Local</div>
      <div class="card-body" style="top:76px">
        <p>Optimizing your local listings and ranking it to the top of local keyword searches is essential to your business!</p>
        <p>It's been proven over and over that local clients who buy our FINDNEARHUB.org services have had the best ROI (return on investment) then any other form of advertising by a mile!</p>
        <p>We know how to get your local listings to the top of local search queries no matter where your local business is located.</p>
        <p class="cta">Order our services today for guaranteed results</p>
      </div>
    </div>

    <div class="ribbon ribbon--right" style="left:400px;top:606px;width:206px;height:44px;padding-left:20px;font-size:22px">Features</div>
    <ul class="features abs" style="left:432px;top:688px;width:350px">
      <li>Complete Website SEO Analysis</li>
      <li>Seekly / Lookwise / Findora local listings</li>
      <li>Website tracking and analytics setup</li>
      <li>Listing Citations/Reviewdeck / 411 / BizPages / CityLists + more</li>
      <li>Business maps and directions for the customers</li>
      <li>Business profile for customer information</li>
      <li>Multiple languages</li>
      <li>Customer reviews</li>
      <li>Customer ratings</li>
      <li>Payment methods</li>
      <li>Photo galleries of the business</li>
      <li>Detailed monthly reporting</li>
      <li>Monthly monitoring and updates</li>
    </ul>
  </section>

  <!-- RIGHT PANEL -->
  <section class="panel panel--right">
    <div class="ribbon ribbon--right" style="left:798px;top:36px;width:246px;height:44px;padding-left:20px;font-size:20px">Our guarantee</div>
    <p class="abs" style="left:814px;top:116px;width:370px">We guarantee that our services are offered exclusive per industry. We will not take on clients in a competing business that operates in the same geo-graphical area. We do NOT charge a separate exclusivity fee. It's just part and parcel of a solid working relationship between us and our clients.</p>

    <div class="panel-card" style="left:813px;top:354px;width:375px;height:306px">
      <div class="card-title" style="height:62px;font-size:25px">Location, Location</div>
      <div class="card-body" style="top:80px">
        <p>In the brick-and-mortar world it has always been about the LOCATION.</p>
        <p>You can now dominate the location factor on a digital level to capture these local, targeted and hot prospects ahead of your competition!</p>
        <p>We know how to get your local listings to the top of search queries no matter where your local business is located.</p>
        <p class="cta">Order our exclusive services today for guaranteed results!</p>
      </div>
    </div>

    <div class="abs" role="img" aria-label="Row of house silhouettes with a magnifying glass over one"
         style="left:860px;top:718px;width:330px;height:156px;background:linear-gradient(180deg,#e2e2e2,#bcbcbc);border-radius:8px"></div>
  </section>
</main>
</body>
</html>
```